Calvin Pruett Insurance Biz Card
Biz card and stationary
Calvin Pruett Insurance Biz Card - Financial Services
Creative Brief
Professional
Calvin Pruett
Independent Agent
Ashford Falls, OH
pruettgroup@lanvex.example.net
www.calvinpruettinsurance.example.com
please use the logo we upload, and keep all font at a size 9 or 10.
please use the content we upload for an example of the back of the card

```html
<!DOCTYPE html>
<html lang="en">
<head>
<meta charset="utf-8">
<title>Calvin Pruett Insurance Stationery</title>
<link href="https://fonts.googleapis.com/css2?family=Libre+Baskerville:ital,wght@0,400;0,700;1,400&display=swap" rel="stylesheet">
<style>
  :root {
    --navy: #1c2a6b;
    --navy-deep: #141f52;
    --taupe: #b3ab98;
    --paper: #ffffff;
    --ink: #3a3f55;
    --muted: #8a8fa3;
    --stage: #e6e7ea;
  }
  * { box-sizing: border-box; margin: 0; padding: 0; }
  html, body { width: 1200px; height: 1054px; overflow: hidden; }
  body {
    background: var(--stage);
    font-family: "Libre Baskerville", Georgia, serif;
    color: var(--ink);
    position: relative;
  }
  .piece {
    position: absolute;
    background: var(--paper);
    overflow: hidden;
    box-shadow: 0 4px 14px rgba(0,0,0,0.15);
  }
  .wave { position: absolute; left: 0; bottom: 0; width: 100%; }
  .wave .stripe { fill: var(--taupe); }
  .wave .band { fill: var(--navy); }

  .brand { display: flex; align-items: center; gap: 10px; }
  .brand-square { background: var(--navy); flex: none; }
  .brand-name { color: var(--navy); font-weight: 700; line-height: 1.1; }

  /* Folder */
  .folder { left: 50px; top: 50px; width: 330px; height: 440px; }
  .folder .brand { position: absolute; left: 40px; top: 70px; }
  .folder .brand-square { width: 46px; height: 46px; }
  .folder .brand-name { font-size: 20px; width: 170px; }
  .folder .site { position: absolute; left: 0; right: 0; bottom: 14px; text-align: center; color: #fff; font-size: 10px; }

  /* Letterhead */
  .letterhead { left: 410px; top: 50px; width: 330px; height: 440px; padding: 30px 30px 0; }
  .letterhead .top { display: flex; justify-content: space-between; align-items: flex-start; }
  .letterhead .brand-square { width: 30px; height: 30px; }
  .letterhead .brand-name { font-size: 12px; width: 100px; }
  .letterhead .contact { font-size: 7px; line-height: 1.6; text-align: right; color: var(--muted); }
  .letterhead .body { margin-top: 34px; font-size: 7.5px; line-height: 1.8; color: var(--ink); }
  .letterhead .body p { margin-bottom: 10px; }
  .letterhead .sign { font-style: italic; color: var(--navy); margin-top: 14px; }
  .letterhead .site { position: absolute; left: 0; right: 0; bottom: 10px; text-align: center; color: #fff; font-size: 8px; }

  /* Envelopes */
  .envelope { left: 770px; width: 380px; height: 200px; }
  .envelope.front { top: 50px; }
  .envelope.front .brand { position: absolute; left: 22px; top: 22px; }
  .envelope .brand-square { width: 30px; height: 30px; }
  .envelope .brand-name { font-size: 12px; width: 110px; }
  .envelope .site { position: absolute; left: 0; right: 0; bottom: 10px; text-align: center; color: #fff; font-size: 8px; }
  .envelope.back { top: 290px; }
  .envelope.back .flap { position: absolute; inset: 0; width: 100%; height: 100%; }
  .envelope.back .brand { position: absolute; left: 50%; top: 70px; transform: translateX(-50%); }

  /* Business cards */
  .card { top: 580px; width: 525px; height: 300px; }
  .card.front { left: 50px; }
  .card.front .brand { position: absolute; left: 30px; top: 32px; }
  .card.front .brand-square { width: 50px; height: 50px; }
  .card.front .brand-name { font-size: 20px; width: 190px; }
  .card.front .agent { position: absolute; left: 303px; top: 98px; }
  .card.front .agent-name { font-size: 19px; font-weight: 700; color: var(--navy); }
  .card.front .agent-title { font-size: 12px; font-style: italic; color: var(--ink); margin-bottom: 14px; }
  .card.front .agent-line { font-size: 11px; line-height: 1.7; color: var(--ink); }
  .card.front .site { position: absolute; left: 30px; top: 130px; font-size: 11px; color: var(--navy); width: 250px; }

  .card.back { left: 625px; background: var(--navy); color: #fff; padding: 34px 34px; }
  .card.back .brand-square { width: 60px; height: 60px; background: var(--paper); position: absolute; left: 34px; top: 40px; }
  .card.back .pitch { margin-left: 86px; font-size: 12px; line-height: 1.6; font-style: italic; }
  .card.back .services { margin-left: 86px; margin-top: 16px; list-style: none; font-size: 11px; line-height: 1.8; }
  .card.back .services li::before { content: "\2013  "; color: var(--taupe); }
  .card.back .site { position: absolute; left: 0; right: 0; bottom: 22px; text-align: center; font-size: 12px; color: var(--taupe); }
</style>
</head>
<body>

<!-- Presentation folder -->
<section class="piece folder">
  <div class="brand">
    <span class="brand-square"></span>
    <span class="brand-name">Calvin Pruett Insurance</span>
  </div>
  <svg class="wave" viewBox="0 0 300 100" preserveAspectRatio="none" height="120">
    <path class="stripe" d="M0 38 C100 8 200 70 300 18 L300 100 L0 100Z"/>
    <path class="band" d="M0 48 C100 20 200 80 300 30 L300 100 L0 100Z"/>
  </svg>
  <div class="site">www.calvinpruettinsurance.example.com</div>
</section>

<!-- Letterhead -->
<section class="piece letterhead">
  <div class="top">
    <div class="brand">
      <span class="brand-square"></span>
      <span class="brand-name">Calvin Pruett Insurance</span>
    </div>
    <div class="contact">
      Ashford Falls, OH<br>
      555-201-0142<br>
      pruettgroup@lanvex.example.net
    </div>
  </div>
  <div class="body">
    <p>Dear Client,</p>
    <p>Thank you for choosing our agency to protect what matters most to you and your family.</p>
    <p>We review every policy each year so your coverage keeps pace with your life and business.</p>
    <p>Please call or write with any questions at all.</p>
    <p>Sincerely,</p>
    <p class="sign">Calvin Pruett</p>
  </div>
  <svg class="wave" viewBox="0 0 300 100" preserveAspectRatio="none" height="80">
    <path class="stripe" d="M0 38 C100 8 200 70 300 18 L300 100 L0 100Z"/>
    <path class="band" d="M0 48 C100 20 200 80 300 30 L300 100 L0 100Z"/>
  </svg>
  <div class="site">www.calvinpruettinsurance.example.com</div>
</section>

<!-- Envelope front -->
<section class="piece envelope front">
  <div class="brand">
    <span class="brand-square"></span>
    <span class="brand-name">Calvin Pruett Insurance</span>
  </div>
  <svg class="wave" viewBox="0 0 300 100" preserveAspectRatio="none" height="70">
    <path class="stripe" d="M0 38 C100 8 200 70 300 18 L300 100 L0 100Z"/>
    <path class="band" d="M0 48 C100 20 200 80 300 30 L300 100 L0 100Z"/>
  </svg>
  <div class="site">www.calvinpruettinsurance.example.com</div>
</section>

<!-- Envelope back -->
<section class="piece envelope back">
  <svg class="flap" viewBox="0 0 380 200" preserveAspectRatio="none">
    <path d="M0 0 L190 60 L380 0" fill="none" stroke="#d6d8de" stroke-width="1.5"/>
  </svg>
  <div class="brand">
    <span class="brand-square"></span>
    <span class="brand-name">Calvin Pruett Insurance</span>
  </div>
  <svg class="wave" viewBox="0 0 300 100" preserveAspectRatio="none" height="70">
    <path class="stripe" d="M0 38 C100 8 200 70 300 18 L300 100 L0 100Z"/>
    <path class="band" d="M0 48 C100 20 200 80 300 30 L300 100 L0 100Z"/>
  </svg>
</section>

<!-- Business card front -->
<section class="piece card front">
  <div class="brand">
    <span class="brand-square"></span>
    <span class="brand-name">Calvin Pruett Insurance</span>
  </div>
  <div class="site">www.calvinpruettinsurance.example.com</div>
  <div class="agent">
    <div class="agent-name">Calvin Pruett</div>
    <div class="agent-title">Independent Agent</div>
    <div class="agent-line">Ashford Falls, OH</div>
    <div class="agent-line">555-201-0142</div>
    <div class="agent-line">pruettgroup@lanvex.example.net</div>
  </div>
  <svg class="wave" viewBox="0 0 300 100" preserveAspectRatio="none" height="80">
    <path class="stripe" d="M0 38 C100 8 200 70 300 18 L300 100 L0 100Z"/>
    <path class="band" d="M0 48 C100 20 200 80 300 30 L300 100 L0 100Z"/>
  </svg>
</section>

<!-- Business card back -->
<section class="piece card back">
  <span class="brand-square"></span>
  <p class="pitch">Insurance solutions that offer the protection and service you need today and help you plan with confidence for the future.</p>
  <ul class="services">
    <li>Home &amp; Auto</li>
    <li>Life &amp; Health</li>
    <li>Business Coverage</li>
    <li>Retirement Planning</li>
  </ul>
  <div class="site">www.calvinpruettinsurance.example.com</div>
</section>

</body>
</html>
```